Company Profile for Consulting Comany

Need Company profile to be designed in a professional way.

for inspiring :-
https://www.vimolia.net/gallery/5307462/COMPANY-PROFILE
https://www.vimolia.net/gallery/20934617/Biotech-Product-Catalog-No1-(Laminar-Air-Flow)
https://www.vimolia.net/gallery/38720954/RKT-Tramvale-Company-Profile-2014-(RKT-Rebrand-part-2)

Target Market(s)

Corporate

Industry/Entity Type

It Company

Font styles to use
Sans Serif

Requirements
Must have
• Landscape A4 size
• Must go with the logo branding
• Must Have Visual Identity is the most important
• Must Have mpty spaces

```html
<!DOCTYPE html>
<html lang="en">
<head>
<meta charset="utf-8">
<title>Company Profile – Pages 5–6</title>
<link href="https://fonts.googleapis.com/css2?family=PT+Sans:wght@400;700&display=swap" rel="stylesheet">
<style>
  :root {
    --stage: #58595b;
    --page-dark: #000000;
    --page-brand: #0f9fc6;
    --band: #ffffff;
    --band-text: #3a3f4a;
    --text-light: #ffffff;
    --text-muted: #e6e6e6;
    --accent: #1a9fd0;
  }
  * { margin: 0; padding: 0; box-sizing: border-box; }
  html, body { width: 1200px; height: 591px; overflow: hidden; }
  body {
    background: var(--stage);
    font-family: "PT Sans", Arial, sans-serif;
    color: var(--text-light);
    position: relative;
  }
  .spread { position: absolute; left: 100px; top: 119px; width: 998px; height: 353px; display: flex; }
  .page { position: relative; height: 100%; }
  .page--services { width: 500px; background: var(--page-dark); }
  .page--partners { width: 498px; background: var(--page-brand); }

  .page-number {
    position: absolute; width: 11px; height: 11px; border-radius: 50%;
    background: var(--accent); color: #fff; font-size: 7px; font-weight: 700;
    display: flex; align-items: center; justify-content: center; line-height: 1;
  }
  .page--services .page-number { left: 20px; top: 171px; }
  .page--partners .page-number { left: 467px; top: 171px; }

  .block-title { font-size: 7.5px; font-weight: 700; text-transform: uppercase; letter-spacing: .2px; margin-bottom: 2px; }
  .block-subtitle { font-size: 6px; font-weight: 700; text-transform: uppercase; margin-top: 6px; margin-bottom: 1px; }
  .body-copy { font-size: 5.4px; line-height: 1.4; color: var(--text-muted); }

  .talent { position: absolute; left: 58px; top: 105px; width: 184px; }
  .hr-solutions { position: absolute; left: 263px; top: 214px; width: 196px; }
  .service-list { list-style: none; margin-top: 5px; padding-left: 12px; }
  .service-list li { font-size: 5.2px; line-height: 1.6; text-transform: uppercase; color: var(--text-muted); position: relative; }
  .service-list li::before { content: ""; position: absolute; left: -7px; top: 3.3px; width: 2px; height: 2px; border-radius: 50%; background: var(--text-muted); }

  .section-title {
    position: absolute; left: 0; right: 0; top: 71px; text-align: center;
    font-size: 16px; font-weight: 700; letter-spacing: .3px;
  }
  .partner-band {
    position: absolute; left: 0; right: 0; top: 157px; height: 38px; background: var(--band);
  }
  .partner-name {
    position: absolute; top: 0; height: 38px; display: flex; align-items: center;
    font-size: 10px; font-weight: 700; color: var(--band-text); white-space: nowrap;
  }
  .partner-name--hca { left: 30px; }
  .partner-name--marlow { left: 122px; }
  .partner-name--stone { left: 215px; }
  .partner-name--quorvia { left: 310px; }
  .partner-name--pellora { left: 398px; }

  .partner-columns { position: absolute; left: 30px; top: 208px; display: flex; gap: 12px; }
  .partner { width: 80px; }
  .partner-title { font-size: 5.6px; font-weight: 700; text-transform: uppercase; line-height: 1.25; margin-bottom: 3px; }
  .partner .body-copy { font-size: 5px; color: #f2f7fa; }
  .partner--last .partner-title { font-weight: 400; }
</style>
</head>
<body>
  <main class="spread">
    <section class="page page--services">
      <span class="page-number">5</span>

      <article class="talent">
        <h2 class="block-title">Talent Assessment</h2>
        <p class="body-copy">Our carefully developed assessment solutions allow you to assess the skills, aptitudes, and abilities of your workforce, enabling you to identify and fill any skills gaps.</p>

        <h3 class="block-subtitle">Talent Assessment:</h3>
        <p class="body-copy">Assessing people for best performance is the most important task of any organization. The quality of assessment ultimately determines the performance of new hires as well as the ability of the organization to deliver on its promises in the market. Using various assessment tools and methods, we can help you devise an assessment strategy linked to job competencies and assessing talent for the purpose of selection and development.</p>

        <h3 class="block-subtitle">Talent Management:</h3>
        <p class="body-copy">As an organization strives to meet its business goals, it must make sure that it has a continuous and integrated process for recruiting, onboarding, developing, and managing talents. We can help you: Identify and implement "best fit" key processes such as performance management, succession management, and employee development, engagement and retention.</p>
      </article>

      <article class="hr-solutions">
        <h2 class="block-title">HR Solutions</h2>
        <p class="body-copy">OUTSOURCING A trusted HRMS solution, combined with regional expertise, now brings you HR Administration and Payroll outsourcing for the Middle East region. Either you are a customized small company with special payroll requirements, or a larger SME seeking confidentiality, accurateness, and timeliness, we have proven ourselves to be a reliable business partner. Our strength in payroll lies in the controls and governance that is put in place.</p>
        <ul class="service-list">
          <li>Employee Relations</li>
          <li>Payroll and Pay</li>
          <li>Merit Increase Processing</li>
          <li>Incentives &amp; Bonus</li>
          <li>Recruitment &amp; Hiring</li>
          <li>Performance Management</li>
        </ul>
      </article>
    </section>

    <section class="page page--partners">
      <h1 class="section-title">SUCCESS PARTNERSHIP</h1>

      <div class="partner-band">
        <span class="partner-name partner-name--hca">HCA</span>
        <span class="partner-name partner-name--marlow">Marlow Ashcombe</span>
        <span class="partner-name partner-name--stone">Stonecurrent</span>
        <span class="partner-name partner-name--quorvia">Quorvia</span>
        <span class="partner-name partner-name--pellora">Pellora</span>
      </div>
      <span class="page-number">6</span>

      <div class="partner-columns">
        <article class="partner">
          <h3 class="partner-title">(HCA) Halden Change Associates, Inc.</h3>
          <p class="body-copy">HCA Halden Change Associates, Inc. (HCA) is an international consulting firm that guides organizations through all types of complex or large-scale change and implementations. Our proprietary Guided Change Pathway (GCP) has been applied extensively in Summit 500 companies and around the world.</p>
        </article>
        <article class="partner">
          <h3 class="partner-title">Marlow Ashcombe</h3>
          <p class="body-copy">Marlow Ashcombe is the only IPDA HR distance learning center that offers ALL modules and ALL units at ALL IPDA qualification levels; They are also approved to offer LMQ qualifications in Coaching and Mentoring and Leadership and management at ALL levels; They have been qualifying HR professionals since 1987, and all our advisors are practicing professionals and Chartered Fellows of IPDA.</p>
        </article>
        <article class="partner">
          <h3 class="partner-title">Stonecurrent</h3>
          <p class="body-copy">With over 20 years industry experience working closely with HR Directors and Managers, we can help your organization achieve its goals by developing stronger, more engaged and sustainable workforces. Our bespoke and flexible Competency Solutions give you the focus and skills to succeed in today's challenging times - and put you in excellent shape for the future. We back this up with a range of support services through our multi-national network of highly experienced consultants.</p>
        </article>
        <article class="partner">
          <h3 class="partner-title">Quorvia</h3>
          <p class="body-copy">Quorvia HCS is a comprehensive Human Capital Management System that streamlines your HR processes. It efficiently administers applicant tracking, benefit programs, workforce training and development, dues calculations and benefits, and ever-changing governmental regulations. The Employee Self-Service (ESS) portal is designed for employee satisfaction as well as operational efficiency.</p>
        </article>
        <article class="partner partner--last">
          <h3 class="partner-title">Pellora Consulting</h3>
          <p class="body-copy">Pellora Consulting is an organization specialized in providing customized Leadership Development solutions to companies in the Middle East and Africa. Recognizing the inability of imported models and solutions to solve problems that face companies in our region, Pellora Consulting builds on international best practices and customizes them to create best fit solutions that are capable of addressing challenges effectively.</p>
        </article>
      </div>
    </section>
  </main>
</body>
</html>
```